Harrow WordPress Design Contest

We need a wordpress design that will incorporate a professional color scheme with company logo in a clean layout. The design needs to consider that this will be developed on a responsive theme. Colors are up to the designer - The green of the logo with black, gray or an accent color. Client wants a 'modern' look.

Industry/Entity Type

It Company

Number of Pages Required

1 page

Font styles to use
Serif
Sans Serif

Requirements
Must have
• Navigation: 1) Home 2) All Auctions 3) Real Estate for Sale 4) Services 5) About Us 6) Contact Us
• Colors - a corporate look with professional color scheme. Green of logo + black and gray, or an eggshell/light beige, or any other accent that keeps within a corporate look.
• In header - logo (attached) , and contact info :5127 Old Tenbury Lane, Scottsville, KY 42190
• 270-555-0143
• Fax: 270-555-0179
• Email:info@harrowlandbidhouse.example
• Design will feature a full width (960 px) slideshow - use a stock photo for real estate.
• Widgets in sidebar or where appropriate - 1) Email Signup 2) Message of the Day 3) Upcoming Auctions 4) News&Events blog 5) Testimonials 6) Social media - QX, chirpo, vidloop, snapboard, zentro+
• Footer will have company logo, association logos (attached) and contact info, with another widget area if necessary
Nice to have
• use of drop down menu styling - Upcoming Auctions / Online Auctions/ Past Auctions under the "Auction Calendar" menu item

```html
<!DOCTYPE html>
<html lang="en">
<head>
<meta charset="utf-8">
<title>Harrow Real Estate Auction</title>
<link href="https://fonts.googleapis.com/css2?family=Open+Sans:ital,wght@0,400;0,600;0,700;1,400&display=swap" rel="stylesheet">
<style>
:root{
  --green:#11652f;
  --green-dark:#0d4f24;
  --ink:#333;
  --muted:#666;
  --topbar:#1f1f1f;
  --footer:#232323;
  --footer-bottom:#1a1a1a;
  --red:#d9453c;
  --red-dark:#c23a32;
  --amber:#f6a623;
  --amber-dark:#e39515;
  --teal:#1c9c6f;
  --teal-dark:#178a61;
  --orange:#e56d16;
  --grey-band:#ececec;
  --line:#dcdcdc;
}
*{box-sizing:border-box;margin:0;padding:0}
html,body{width:1200px;height:2368px;overflow:hidden}
body{position:relative;background:#fff;font-family:"Open Sans",Arial,sans-serif;color:var(--ink)}
.abs{position:absolute}

/* top bar */
.topbar{left:0;top:0;width:1200px;height:28px;background:var(--topbar);color:#ddd;font-size:11.5px}
.topbar .item{position:absolute;top:7px;display:flex;align-items:center;gap:7px}
.topbar svg{width:12px;height:12px;fill:#eee}

/* header */
.header{left:0;top:28px;width:1200px;height:95px;background:#fff}
.logo{position:absolute;left:98px;top:10px;display:flex;align-items:center;gap:8px}
.logo .mark{width:22px;height:22px;background:var(--green)}
.logo .name{font-size:30px;font-weight:700;color:var(--green);letter-spacing:.5px}
.nav{position:absolute;top:42px;font-size:13px;color:#444}
.nav span{position:absolute;white-space:nowrap}
.nav .caret{width:9px;height:9px;margin-left:6px;vertical-align:middle}

/* hero */
.hero{left:0;top:123px;width:1200px;height:457px;
  background:linear-gradient(90deg,rgba(255,190,70,.35) 0%,rgba(255,190,70,.15) 40%,rgba(0,0,0,0) 65%),
  linear-gradient(180deg,#2c4fb3 0%,#1d3580 35%,#152650 60%,#2f3426 80%,#3a3d24 100%)}
.hero .title{position:absolute;left:670px;top:62px;color:#fff;font-size:28px;font-weight:600;letter-spacing:.3px}
.hero .lede{position:absolute;left:670px;top:104px;width:460px;color:#e8ecf6;font-size:16px;line-height:27px;text-transform:uppercase}
.hero .arrow{position:absolute;top:204px;width:32px;height:32px;border-radius:50%;background:rgba(255,255,255,.25)}
.hero .arrow svg{width:32px;height:32px;stroke:#fff;fill:none;stroke-width:2}

.dropdown{left:494px;top:141px;width:176px;height:118px;background:#fff;border-radius:3px;box-shadow:0 2px 6px rgba(0,0,0,.2);font-size:11.5px;color:#444}
.dropdown span{position:absolute;left:12px}

/* quick links */
.quick{top:611px;height:65px;width:267px;color:#fff;display:flex;align-items:center}
.quick .icon{width:58px;height:65px;display:flex;align-items:center;justify-content:center}
.quick .icon svg{width:24px;height:24px;fill:none;stroke:#fff;stroke-width:1.8}
.quick .text{padding-left:24px}
.quick .label{font-size:13.5px;font-weight:700;text-transform:uppercase}
.quick .sub{font-size:11px;margin-top:2px}
.q-red{left:188px;background:var(--red)} .q-red .icon{background:var(--red-dark)}
.q-amber{left:467px;background:var(--amber)} .q-amber .icon{background:var(--amber-dark)}
.q-teal{left:745px;background:var(--teal)} .q-teal .icon{background:var(--teal-dark)}

/* headings */
.section-title{font-size:15px;font-weight:700;color:#222;text-transform:uppercase}
.section-lede{font-size:12.5px;color:#555}

/* auctions */
.listing{width:254px}
.listing .photo{width:254px;height:151px}
.listing .city{margin-top:17px;font-size:13px;font-weight:700;color:var(--green)}
.listing .company{margin-top:5px;font-size:12px;color:#555}
.listing .details{margin-top:6px;font-size:11.5px;font-weight:600;color:var(--green-dark);display:flex;align-items:center;gap:5px}
.listing .details svg{width:10px;height:10px}

.btn-more{left:520px;top:1315px;width:161px;height:37px;background:var(--orange);color:#fff;font-size:11px;font-weight:700;display:flex;align-items:center;justify-content:center;border-radius:2px;box-shadow:0 2px 0 #b9530d}
.divider{left:188px;top:1380px;width:824px;height:2px;background:var(--line)}

/* testimonials */
.widget-title{font-size:13px;font-weight:700;color:var(--green-dark);text-transform:uppercase}
.pager{font-size:12px;color:#aaa;letter-spacing:6px}
.quote{width:264px;height:121px;background:#f0f0f0;border:1px solid #d6d6d6;border-radius:3px;padding:24px 26px;font-size:11px;font-style:italic;line-height:25px;color:#555}
.person{display:flex;align-items:center;gap:18px}
.person .avatar{width:56px;height:52px;background:linear-gradient(180deg,#e7e9ec,#c9ccd1)}
.person .name{font-size:12.5px;font-weight:700;color:var(--green)}
.person .role{font-size:11px;color:#555;margin-top:4px}
.motd .item{border-bottom:1px solid var(--line);padding-bottom:14px;margin-bottom:16px}
.motd .head{font-size:10.5px;font-weight:700;color:#222;text-transform:uppercase}
.motd .body{font-size:11.5px;color:#555;line-height:22px;margin-top:10px}

/* news band */
.news-band{left:0;top:1690px;width:1200px;height:338px;background:var(--grey-band)}
.post{width:193px}
.post .photo{width:193px;height:131px}
.post .head{margin-top:16px;font-size:10.5px;font-weight:700;color:var(--green);text-transform:uppercase}
.post .date{margin-top:6px;font-size:11.5px;color:#555}

/* footer */
.footer{left:0;top:2028px;width:1200px;height:293px;background:var(--footer);color:#999}
.footer h4{position:absolute;top:47px;font-size:12px;font-weight:700;color:#fff;text-transform:uppercase}
.footer .hint{position:absolute;left:125px;top:81px;font-size:10.5px;font-style:italic;color:#aaa}
.footer .field{position:absolute;left:126px;width:256px;height:35px;background:#fff;border-radius:3px;font-size:11px;color:#444;padding:10px 14px}
.footer .subscribe{position:absolute;left:126px;top:211px;width:111px;height:35px;background:var(--orange);color:#fff;border-radius:2px;font-size:11px;font-weight:700;display:flex;align-items:center;justify-content:center}
.footer .links span{position:absolute;font-size:11.5px;color:#aaa}
.footer .badge{position:absolute;top:214px;height:44px;background:#f4f4f4}
.footer .social{position:absolute;left:952px;display:flex;align-items:center;gap:8px;font-size:11.5px;color:#aaa}
.footer .social i{display:block;width:26px;height:26px;border-radius:50%;background:#555}
.bottom{left:0;top:2321px;width:1200px;height:47px;background:var(--footer-bottom);color:#888;font-size:11.5px;display:flex;align-items:center;justify-content:center}
</style>
</head>
<body>

<div class="abs topbar">
  <div class="item" style="left:98px"><svg viewBox="0 0 24 24"><path d="M6.6 10.8a15 15 0 0 0 6.6 6.6l2.2-2.2c.3-.3.7-.4 1-.2 1.1.4 2.3.6 3.6.6.6 0 1 .4 1 1V20c0 .6-.4 1-1 1A17 17 0 0 1 3 4c0-.6.4-1 1-1h3.5c.6 0 1 .4 1 1 0 1.3.2 2.5.6 3.6.1.3 0 .7-.2 1z"/></svg>Call Us : 270-555-0143</div>
  <div class="item" style="left:272px"><svg viewBox="0 0 24 24"><path d="M6 3h9l3 3v4h2a1 1 0 0 1 1 1v9a1 1 0 0 1-1 1H4a1 1 0 0 1-1-1v-9a1 1 0 0 1 1-1h2zm2 2v5h8V7h-2V5zm-1 9v2h3v-2zm5 0v2h5v-2z"/></svg>Fax us : 270-555-0179</div>
  <div class="item" style="left:430px"><svg viewBox="0 0 24 24"><path d="M3 5h18v14H3zm2 2v.5l7 4.5 7-4.5V7l-7 4.5z"/></svg>Email Us : info@harrowlandbidhouse.example</div>
  <div class="item" style="left:850px"><svg viewBox="0 0 24 24"><path d="M12 2a7 7 0 0 1 7 7c0 5-7 13-7 13S5 14 5 9a7 7 0 0 1 7-7zm0 4.5a2.5 2.5 0 1 0 0 5 2.5 2.5 0 0 0 0-5z"/></svg>5127 Old Tenbury Lane, Scottsville, KY 42190</div>
</div>

<header class="abs header">
  <div class="logo"><span class="mark"></span><span class="name">Harrow</span></div>
  <nav class="nav">
    <span style="left:394px">Home</span>
    <span style="left:494px">All Auctions<svg class="caret" viewBox="0 0 10 10"><path d="M1 3l4 4 4-4" fill="none" stroke="#444" stroke-width="1.4"/></svg></span>
    <span style="left:627px">Real Estate for Sale</span>
    <span style="left:805px">Services</span>
    <span style="left:917px">About Us</span>
    <span style="left:1036px">Contact Us</span>
  </nav>
</header>

<section class="abs hero" role="img" aria-label="Slideshow photo: modern two-storey house lit warmly at dusk beneath a deep blue sky">
  <div class="arrow" style="left:-12px"><svg viewBox="0 0 32 32"><path d="M19 9l-7 7 7 7"/></svg></div>
  <div class="arrow" style="left:1134px"><svg viewBox="0 0 32 32"><path d="M13 9l7 7-7 7"/></svg></div>
  <h1 class="title">HARROW REAL ESTATE AUCTION</h1>
  <p class="lede">Lorem ipsum is simply dummy text of the printing and typesetting industry.</p>
</section>

<div class="abs dropdown">
  <span style="top:18px">›&nbsp; Upcoming Auctions</span>
  <span style="top:47px">›&nbsp; Online Auctions</span>
  <span style="top:76px">›&nbsp; Past Auctions</span>
</div>

<a class="abs quick q-red">
  <span class="icon"><svg viewBox="0 0 24 24"><path d="M6 2h9l4 4v16H6zM9 10h7M9 14h7M9 18h7"/></svg></span>
  <span class="text"><div class="label">Search All Listings</div><div class="sub">Click here for view list »</div></span>
</a>
<a class="abs quick q-amber">
  <span class="icon"><svg viewBox="0 0 24 24" style="fill:#fff;stroke:none"><path d="M12 3l10 9h-3v9h-5v-6h-4v6H5v-9H2z"/></svg></span>
  <span class="text"><div class="label">Residential Listings</div><div class="sub">Click here for view list »</div></span>
</a>
<a class="abs quick q-teal">
  <span class="icon"><svg viewBox="0 0 24 24" style="fill:#fff;stroke:none"><path d="M11 22V10h2v12zM12 9c-3 0-4-3-4-6 3 0 4 3 4 6zm0 0c0-3 1-6 4-6 0 3-1 6-4 6zm-1 5c-3 0-5-2-5-5 3 0 5 2 5 5zm2 0c0-3 2-5 5-5 0 3-2 5-5 5zm-2 5c-3 0-5-2-5-5 3 0 5 2 5 5zm2 0c0-3 2-5 5-5 0 3-2 5-5 5z"/></svg></span>
  <span class="text"><div class="label">Land Listings</div><div class="sub">Click here for view list »</div></span>
</a>

<h2 class="abs section-title" style="left:188px;top:725px">Upcoming Auctions</h2>
<p class="abs section-lede" style="left:188px;top:755px">Simply dummy text of the printing and typesetting industry. Lorem Ipsum has been the industry's standard dummy...</p>

<div class="abs listing" style="left:188px;top:796px"><div class="photo" role="img" aria-label="Photo: modern house with lit pool at night" style="background:linear-gradient(180deg,#1b2f6a,#3a4a58 55%,#2aa9d9)"></div><div class="city">BLOOMINGTON, TN</div><div class="company">Harrow Real Estate &amp; Auction Co.</div><div class="details">View Details <svg viewBox="0 0 10 10"><circle cx="5" cy="5" r="5" fill="#0d4f24"/><path d="M4 3l2 2-2 2" stroke="#fff" fill="none"/></svg></div></div>
<div class="abs listing" style="left:472px;top:796px"><div class="photo" role="img" aria-label="Photo: white modern villa by the sea" style="background:linear-gradient(180deg,#5d93c4,#dfe7ee 50%,#9a9a9a)"></div><div class="city">BLOOMINGTON, TN</div><div class="company">Harrow Real Estate &amp; Auction Co.</div><div class="details">View Details <svg viewBox="0 0 10 10"><circle cx="5" cy="5" r="5" fill="#0d4f24"/><path d="M4 3l2 2-2 2" stroke="#fff" fill="none"/></svg></div></div>
<div class="abs listing" style="left:756px;top:796px"><div class="photo" role="img" aria-label="Photo: white villa with palm trees at dusk" style="background:linear-gradient(180deg,#27477e,#8aa0bd 45%,#d9cdb8 75%,#4d4a3e)"></div><div class="city">BLOOMINGTON, TN</div><div class="company">Harrow Real Estate &amp; Auction Co.</div><div class="details">View Details <svg viewBox="0 0 10 10"><circle cx="5" cy="5" r="5" fill="#0d4f24"/><path d="M4 3l2 2-2 2" stroke="#fff" fill="none"/></svg></div></div>

<div class="abs listing" style="left:188px;top:1053px"><div class="photo" role="img" aria-label="Photo: terrace lounge overlooking a mountain lake" style="background:linear-gradient(180deg,#9ab1c6,#7f8f87 45%,#2b2b2b)"></div><div class="city">BLOOMINGTON, TN</div><div class="company">Harrow Real Estate &amp; Auction Co.</div><div class="details">View Details <svg viewBox="0 0 10 10"><circle cx="5" cy="5" r="5" fill="#0d4f24"/><path d="M4 3l2 2-2 2" stroke="#fff" fill="none"/></svg></div></div>
<div class="abs listing" style="left:472px;top:1053px"><div class="photo" role="img" aria-label="Photo: cream Mediterranean mansion with pool" style="background:linear-gradient(180deg,#4f8cc9,#e9dfcc 45%,#d4c2a2 80%,#3aa6c5)"></div><div class="city">BLOOMINGTON, TN</div><div class="company">Harrow Real Estate &amp; Auction Co.</div><div class="details">View Details <svg viewBox="0 0 10 10"><circle cx="5" cy="5" r="5" fill="#0d4f24"/><path d="M4 3l2 2-2 2" stroke="#fff" fill="none"/></svg></div></div>
<div class="abs listing" style="left:756px;top:1053px"><div class="photo" role="img" aria-label="Photo: modern white house with pool deck" style="background:linear-gradient(180deg,#a9c4da,#eef1f2 50%,#29a9dc 85%,#8d7157)"></div><div class="city">BLOOMINGTON, TN</div><div class="company">Harrow Real Estate &amp; Auction Co.</div><div class="details">View Details <svg viewBox="0 0 10 10"><circle cx="5" cy="5" r="5" fill="#0d4f24"/><path d="M4 3l2 2-2 2" stroke="#fff" fill="none"/></svg></div></div>

<a class="abs btn-more">VIEW MORE LISTING</a>
<div class="abs divider"></div>

<h3 class="abs widget-title" style="left:190px;top:1413px">Testimonials</h3>
<span class="abs pager" style="left:724px;top:1411px">‹›</span>
<div class="abs quote" style="left:190px;top:1450px">It is a long established fact that a reader will be distracted by the readable content of a page when looking at its layout...</div>
<div class="abs quote" style="left:486px;top:1450px">It is a long established fact that a reader will be distracted by the readable content of a page when looking at its layout...</div>
<div class="abs person" style="left:192px;top:1588px"><div class="avatar" role="img" aria-label="Portrait of client"></div><div><div class="name">Colin Avery</div><div class="role">Marketing Executive</div></div></div>
<div class="abs person" style="left:488px;top:1588px"><div class="avatar" role="img" aria-label="Portrait of client"></div><div><div class="name">Colin Avery</div><div class="role">Marketing Executive</div></div></div>

<h3 class="abs widget-title" style="left:780px;top:1413px">Message of the Day</h3>
<span class="abs pager" style="left:988px;top:1411px">‹›</span>
<div class="abs motd" style="left:782px;top:1450px;width:230px">
  <div class="item"><div class="head">Long Established Fact</div><div class="body">It is a long established fact that a reader will be distracted by the readable...</div></div>
  <div class="item"><div class="head">Long Established Fact</div><div class="body">It is a long established fact that a reader will be distracted by the readable...</div></div>
</div>

<section class="abs news-band">
  <h2 class="abs section-title" style="left:188px;top:43px">News&amp;Events Blog</h2>
  <p class="abs section-lede" style="left:188px;top:72px">Simply dummy text of the printing and typesetting industry. Lorem Ipsum has been the industry's standard dummy...</p>
  <div class="abs post" style="left:188px;top:112px"><div class="photo" role="img" aria-label="Photo: modern house at dusk" style="background:linear-gradient(180deg,#1c3f8f,#4a5a78 55%,#3b3024)"></div><div class="head">Lorem Ipsum is a dummy</div><div class="date">Posted on 27 March 2015</div></div>
  <div class="abs post" style="left:398px;top:112px"><div class="photo" role="img" aria-label="Photo: guests toasting with wine" style="background:linear-gradient(135deg,#2a1a12,#6b4a30 55%,#1a120c)"></div><div class="head">Lorem Ipsum is a dummy</div><div class="date">Posted on 27 March 2015</div></div>
  <div class="abs post" style="left:608px;top:112px"><div class="photo" role="img" aria-label="Photo: villa with pool at twilight" style="background:linear-gradient(180deg,#3d6fc4,#7f8fa8 45%,#2e95c8)"></div><div class="head">Lorem Ipsum is a dummy</div><div class="date">Posted on 27 March 2015</div></div>
  <div class="abs post" style="left:818px;top:112px"><div class="photo" role="img" aria-label="Photo: dinner party around a table" style="background:linear-gradient(135deg,#3a2418,#8a5a3a 50%,#2a1a12)"></div><div class="head">Lorem Ipsum is a dummy</div><div class="date">Posted on 27 March 2015</div></div>
</section>

<footer class="abs footer">
  <h4 style="left:125px">Newletter Signup</h4>
  <p class="hint">Get our recent updates through your email id</p>
  <div class="field" style="top:108px">Enter your Name</div>
  <div class="field" style="top:157px">Enter your email id</div>
  <div class="subscribe">SUBSCRIBE</div>

  <h4 style="left:513px">Welcome</h4>
  <div class="links">
    <span style="left:513px;top:74px">Home</span>
    <span style="left:513px;top:96px">All Auctions</span>
    <span style="left:513px;top:118px">Real Estate for Sale</span>
    <span style="left:513px;top:140px">Services</span>
    <span style="left:513px;top:162px">About Us</span>
    <span style="left:513px;top:184px">Contact Us</span>
  </div>
  <div class="badge" style="left:513px;width:60px"></div>
  <div class="badge" style="left:633px;width:86px;border-radius:50%"></div>
  <div class="badge" style="left:743px;width:94px"></div>

  <h4 style="left:726px">Information</h4>
  <div class="links">
    <span style="left:726px;top:74px">Privacy Policy</span>
    <span style="left:726px;top:96px">Terms &amp; Conditions</span>
    <span style="left:726px;top:118px">Sitemap</span>
  </div>

  <h4 style="left:952px">Follow Us</h4>
  <div class="social" style="top:71px"><i></i>: QX</div>
  <div class="social" style="top:111px"><i></i>: chirpo</div>
  <div class="social" style="top:152px"><i></i>: vidloop</div>
  <div class="social" style="top:193px"><i></i>: snapboard</div>
  <div class="social" style="top:233px"><i></i>: zentro+</div>
</footer>

<div class="abs bottom">© 2015. Harrow real estate auction. All rights reserved.</div>

</body>
</html>
```